Business Card Design Project

business cards to match the logo design reference 1970674
specific details to be provided asap - message to follow
hello - thank you for the logo design (reference 1970674) which we are very happy with. In terms of business cards you presented a couple of options ie blue front/white back and then the reverse. Can we start with the white front version but change the text details to black font?
Actual details are as follows;
Dorian Whitcombe
Managing Director
e dorianwhitcombe@velantra.com.au
t +61 2 7315 2946
m +61 422 517 639
Suite 307, Level 3, 82 Penhallow St
Sydney, NSW 2000, Australia
www.velantra.com.au

```html
<!DOCTYPE html>
<html lang="en">
<head>
<meta charset="utf-8">
<title>Velantra Business Cards</title>
<link rel="stylesheet" href="https://fonts.googleapis.com/css2?family=Exo+2:wght@400;500;600&display=swap">
<style>
  :root {
    --backdrop: #2a2a2c;
    --brand-blue: #1f78c4;
    --brand-blue-deep: #1766ab;
    --brand-blue-soft: #7fa6d6;
    --label-blue: #2a6fb6;
    --card-white: #f4f4f4;
    --card-white-edge: #dcdcdc;
    --ink: #111111;
    --on-blue: #e8f2fb;
  }
  * { box-sizing: border-box; margin: 0; padding: 0; }
  html, body { width: 1200px; height: 900px; overflow: hidden; }
  body {
    background: var(--backdrop);
    font-family: "Exo 2", sans-serif;
    position: relative;
  }
  .card {
    position: absolute;
    width: 560px;
    height: 320px;
    box-shadow: 0 10px 30px rgba(0,0,0,0.55);
  }
  .card-front {
    left: 100px;
    top: 100px;
    background: linear-gradient(160deg, var(--brand-blue) 0%, var(--brand-blue-deep) 100%);
    color: var(--on-blue);
  }
  .brand-lockup {
    position: absolute;
    left: 92px;
    top: 118px;
    display: flex;
    align-items: center;
    gap: 26px;
  }
  .brand-mark {
    width: 70px;
    height: 70px;
    border-radius: 50%;
    background: var(--on-blue);
  }
  .brand-name {
    font-size: 62px;
    font-weight: 600;
    letter-spacing: 1px;
    color: var(--on-blue);
  }
  .front-web {
    position: absolute;
    right: 26px;
    bottom: 18px;
    font-size: 17px;
    letter-spacing: 0.5px;
  }
  .card-back {
    left: 540px;
    top: 480px;
    background: linear-gradient(170deg, #ffffff 0%, var(--card-white) 60%, var(--card-white-edge) 100%);
    color: var(--ink);
  }
  .person {
    position: absolute;
    left: 34px;
    top: 40px;
  }
  .person-name {
    font-size: 34px;
    font-weight: 500;
    letter-spacing: 1px;
    text-transform: uppercase;
    line-height: 1;
  }
  .person-title {
    font-size: 20px;
    font-weight: 500;
    margin-top: 4px;
  }
  .address {
    position: absolute;
    left: 34px;
    top: 130px;
    font-size: 15px;
    line-height: 1.3;
  }
  .contact {
    position: absolute;
    left: 34px;
    bottom: 26px;
    font-size: 15px;
    line-height: 1.35;
    list-style: none;
  }
  .contact-email { margin-bottom: 20px; }
  .contact-label { color: var(--label-blue); margin-right: 4px; }
  .back-mark {
    position: absolute;
    right: 50px;
    top: 50px;
    width: 140px;
    height: 140px;
    border-radius: 50%;
    background: var(--brand-blue-soft);
  }
</style>
</head>
<body>
  <section class="card card-front" aria-label="Card front">
    <div class="brand-lockup">
      <span class="brand-mark"></span>
      <span class="brand-name">Velantra</span>
    </div>
    <p class="front-web">www.velantra.com.au</p>
  </section>

  <section class="card card-back" aria-label="Card back">
    <div class="person">
      <h1 class="person-name">Dorian Whitcombe</h1>
      <p class="person-title">Managing Director</p>
    </div>
    <p class="address">Suite 307, Level 3, 82 Penhallow St<br>Sydney, NSW 2000, Australia</p>
    <ul class="contact">
      <li class="contact-email">dorianwhitcombe@velantra.com.au</li>
      <li><span class="contact-label">E:</span>dorianwhitcombe@velantra.com.au</li>
      <li><span class="contact-label">T:</span>+61 2 7315 2946</li>
      <li><span class="contact-label">M:</span>+61 422 517 639</li>
    </ul>
    <span class="back-mark"></span>
  </section>
</body>
</html>
```